Property Development Business Cards

I need a business card design for Blue Harbour Developments Pty Ltd. We are a property development company in Australia and our name defines the five values that we adhere to, being Profitable, Partnerships, Quality Developments, Eco Friendly and Enduring Design.

I have attached the current logo that I use, it is just five yellow circles connected to a single cricle in the middle.

Target Market(s)

Our Target audience is real estate agents, owners of properties, builders and other trades

Industry/Entity Type

Business

Requirements
Must have
• Want to have two sides to the card, one with details and one to just highlight the company

```html
<!DOCTYPE html>
<html lang="en">
<head>
<meta charset="utf-8">
<title>Blue Harbour Developments – Business Cards</title>
<link rel="stylesheet" href="https://fonts.googleapis.com/css2?family=Arimo:wght@400;700&display=swap">
<style>
  :root {
    --stage: #2b2f33;
    --navy-deep: #0c3152;
    --navy-mid: #175f8c;
    --navy-light: #1f7aab;
    --accent-yellow: #f5c400;
    --card-grey: #d9dadc;
    --card-grey-light: #e6e7e8;
    --white: #ffffff;
    --name-grey: #7a7c80;
    --text-dark: #2f3134;
    --text-grey: #8a8c90;
  }
  * { margin: 0; padding: 0; box-sizing: border-box; }
  html, body {
    width: 1200px; height: 720px; overflow: hidden;
    background: var(--stage);
    font-family: "Arimo", Arial, sans-serif;
  }
  .canvas {
    position: relative; width: 1200px; height: 720px;
  }
  .card {
    position: absolute;
    width: 540px; height: 300px;
    top: 210px;
    border-radius: 12px;
    overflow: hidden;
    box-shadow: 0 10px 30px rgba(0,0,0,0.45);
  }

  /* Front: brand side */
  .card--front {
    left: 50px;
    background: radial-gradient(ellipse 60% 70% at 50% 42%, var(--navy-light) 0%, var(--navy-mid) 40%, var(--navy-deep) 100%);
    display: flex; flex-direction: column; align-items: center; justify-content: center;
    color: var(--white);
    text-align: center;
  }
  .brand-dot {
    width: 52px; height: 52px; border-radius: 50%;
    background: var(--accent-yellow);
    margin-bottom: 22px;
  }
  .brand-name {
    font-weight: 700; color: var(--white);
    line-height: 1;
  }
  .card--front .brand-name__main { font-size: 40px; letter-spacing: -1.5px; }
  .card--front .brand-name__sub { font-size: 21px; letter-spacing: -0.6px; margin-top: 4px; }

  /* Back: details side */
  .card--back {
    left: 610px;
    background: var(--card-grey);
  }
  .card-back__shapes { position: absolute; inset: 0; }
  .card-back__brand {
    position: absolute; left: 30px; top: 105px; width: 230px;
    display: flex; flex-direction: column; align-items: center;
    text-align: center;
  }
  .card-back__brand .brand-dot { width: 38px; height: 38px; margin-bottom: 16px; }
  .card-back__brand .brand-name__main { font-size: 29px; letter-spacing: -1.2px; }
  .card-back__brand .brand-name__sub { font-size: 15.5px; letter-spacing: -0.5px; margin-top: 3px; }
  .website {
    position: absolute; left: 32px; top: 240px;
    font-size: 12px; color: var(--white); letter-spacing: -0.3px;
  }
  .website strong { font-size: 14px; font-weight: 700; }

  .contact {
    position: absolute; right: 56px; text-align: right;
    color: var(--text-dark);
  }
  .contact--person { top: 30px; }
  .contact__name {
    font-size: 20px; font-weight: 700; color: var(--name-grey); letter-spacing: 0.2px;
  }
  .contact__mobile { font-size: 15px; margin-top: 5px; }
  .contact--address { top: 212px; font-size: 15px; line-height: 21px; }

  .email-rule {
    position: absolute; right: 42px; top: 22px; bottom: 24px;
    width: 1px; background: var(--text-grey);
  }
  .email {
    position: absolute; right: 16px; top: 20px;
    writing-mode: vertical-rl;
    font-size: 15px; font-weight: 700; color: var(--text-grey); letter-spacing: 0.4px;
  }
</style>
</head>
<body>
<main class="canvas">

  <section class="card card--front" aria-label="Card front">
    <div class="brand-dot"></div>
    <div class="brand-name brand-name__main">Blue Harbour</div>
    <div class="brand-name brand-name__sub">Developments Pty Ltd</div>
  </section>

  <section class="card card--back" aria-label="Card back">
    <svg class="card-back__shapes" viewBox="0 0 540 300" preserveAspectRatio="none" aria-hidden="true">
      <defs>
        <radialGradient id="backNavy" cx="40%" cy="45%" r="65%">
          <stop offset="0" stop-color="#1f7aab"/>
          <stop offset="0.45" stop-color="#175f8c"/>
          <stop offset="1" stop-color="#0c3152"/>
        </radialGradient>
      </defs>
      <path d="M0 0 H172 C250 60 330 180 392 300 H0 Z" fill="#ffffff"/>
      <path d="M0 0 H158 C236 62 314 180 374 300 H0 Z" fill="url(#backNavy)"/>
      <path d="M0 300 V272 C40 250 160 250 240 262 C300 272 340 286 374 300 Z" fill="#e6e7e8"/>
    </svg>

    <div class="card-back__brand">
      <div class="brand-dot"></div>
      <div class="brand-name brand-name__main">Blue Harbour</div>
      <div class="brand-name brand-name__sub">Developments Pty Ltd</div>
    </div>
    <div class="website">www.<strong>blueharbourdev</strong>.com.au</div>

    <div class="contact contact--person">
      <div class="contact__name">Daniel Marsh</div>
      <div class="contact__mobile">Mobile: 0400 555 218</div>
    </div>
    <div class="contact contact--address">
      PO Box 127<br>Hallett<br>ACT 2915
    </div>

    <div class="email-rule"></div>
    <div class="email">daniel@blueharbourdev.com.au</div>
  </section>

</main>
</body>
</html>
```